Introduction of new dentist and new treatments

We want inform our Patients of our new dentist and new treatment methods. It is dealing about biologic dentistry and holistic dentistry. we are in switzerland and speak german

Font styles to use
Sans Serif

Colors
00a990
33b8a4
9bcb3c
acd036
cadf82
0292cd
3176b5
e34297
e667a6

Requirements
Must have
• Text, which can be edited. It will be in german
• Name of the dental clinic is
• "Brivana - Ihr Zahnarzt in Zug"
Nice to have
• A4 Layout

```html
<!DOCTYPE html>
<html lang="de">
<head>
<meta charset="utf-8">
<title>Brivana – Ihr Zahnarzt in Zug</title>
<link href="https://fonts.googleapis.com/css2?family=Montserrat:wght@800;900&family=Source+Sans+3:wght@400;600&display=swap" rel="stylesheet">
<style>
:root{
  --stage:#c2c2c2;
  --paper:#f7f7f7;
  --panel:#ececec;
  --green:#4fb958;
  --blue:#1479c4;
  --heading-blue:#1a7ac4;
  --navy:#2b3550;
  --ink:#222;
  --white:#fff;
}
*{margin:0;padding:0;box-sizing:border-box}
html,body{width:1200px;height:1200px;overflow:hidden;background:var(--stage)}
.flyer{position:absolute;left:136px;top:0;width:927px;height:1200px;background:var(--paper);overflow:hidden;font-family:"Source Sans 3",sans-serif;color:var(--ink)}
.panel{position:absolute;left:0;top:461px;width:927px;height:330px;background:var(--panel)}
.hero-art{position:absolute;left:0;top:0;width:927px;height:560px}
.brand{position:absolute;left:60px;top:104px;width:220px;text-align:center}
.brand-name{font-weight:400;font-size:26px;letter-spacing:5px;color:var(--navy);display:flex;align-items:center;justify-content:center;gap:8px}
.brand-dot{width:10px;height:10px;border-radius:50%;background:var(--blue)}
.brand-tag{font-size:12px;color:var(--navy);margin-top:4px}
.hero-title{position:absolute;left:21px;top:211px;width:362px;font-family:"Montserrat",sans-serif;font-weight:900;font-size:17px;line-height:23px;color:var(--white);text-align:justify}
.hero-lead{position:absolute;left:21px;top:320px;width:430px;font-size:17px;line-height:23px;color:var(--white);text-align:justify}
.section{position:absolute}
.section h2{font-family:"Montserrat",sans-serif;font-weight:900;font-size:19px;line-height:25px;color:var(--heading-blue);position:relative;text-align:justify}
.section h2 .star{position:absolute;left:-27px;top:2px;width:18px;height:18px}
.section p{font-size:15.5px;line-height:20px;text-align:justify;hyphens:auto}
.col-left{left:47px;top:498px;width:409px}
.col-right{left:517px;top:502px;width:386px}
.divider{position:absolute;left:481px;top:495px;width:2px;height:275px;background:#999}
.wide{left:47px;width:850px}
.wide p{font-size:13.5px;line-height:18px}
.sec-3{top:808px}
.sec-4{top:906px}
.footer-band{position:absolute;left:142px;top:1043px;width:785px;height:110px;background:var(--blue)}
.footer-call{position:absolute;left:150px;top:1065px;width:777px;text-align:center;color:var(--white);font-size:19px;font-weight:600}
.footer-contact{position:absolute;left:150px;top:1100px;width:777px;display:flex;justify-content:center;gap:22px;color:var(--white);font-family:"Montserrat",sans-serif;font-weight:800;font-size:24px;line-height:32px}
.footer-contact span{display:flex;align-items:center;gap:8px}
.footer-contact svg{width:16px;height:22px}
.portrait{position:absolute;left:18px;top:1017px;width:156px;height:156px;border-radius:50%;border:4px solid var(--blue);background:radial-gradient(circle at 50% 40%,#d9d6d2,#a9a7a5)}
</style>
</head>
<body>
<div class="flyer">
  <div class="panel"></div>

  <svg class="hero-art" viewBox="0 0 927 560">
    <defs>
      <linearGradient id="familyTone" x1="0" y1="0" x2="1" y2="1">
        <stop offset="0" stop-color="#f3ddc8"/>
        <stop offset="0.5" stop-color="#e2b996"/>
        <stop offset="1" stop-color="#f4ece4"/>
      </linearGradient>
      <radialGradient id="smileTone" cx="0.5" cy="0.5" r="0.6">
        <stop offset="0" stop-color="#f4f1ee"/>
        <stop offset="0.55" stop-color="#d22a2a"/>
        <stop offset="1" stop-color="#f1d6cc"/>
      </radialGradient>
    </defs>
    <path fill="var(--green)" d="M0,162 C120,148 250,150 342,162 C420,260 470,400 620,455 C660,470 700,480 742,493 C560,500 400,470 260,465 C150,461 60,461 0,461 Z"/>
    <path role="img" aria-label="Foto einer lachenden Familie mit zwei Kindern" fill="url(#familyTone)" d="M342,0 H927 V420 C860,450 760,470 690,460 C600,440 520,380 475,300 C430,220 385,110 342,0 Z"/>
    <circle cx="824" cy="347" r="125" fill="var(--white)"/>
    <circle role="img" aria-label="Nahaufnahme eines Lächelns mit weissen Zähnen" cx="824" cy="347" r="117" fill="url(#smileTone)"/>
  </svg>

  <div class="brand">
    <div class="brand-name"><span class="brand-dot"></span>BRIVANA</div>
    <div class="brand-tag">Ihr Zahnarzt in Zug</div>
  </div>

  <h1 class="hero-title">Interdisziplinäre Zahnmedizin - Zusammenhang zwischen Zahn­problemen und der Gesundheit von Körper und Geist</h1>
  <p class="hero-lead">Zahn und Gesundheit haben eins gemeinsam – Man vermisst sie, wenn sie fehlt. Zähne haben einen engen Zusammenhang zur Gesundheit und können diese beeinflussen. Sowohl negativ als auch positiv.</p>

  <div class="section col-left">
    <h2><svg class="star" viewBox="0 0 20 20"><path fill="var(--green)" d="M10 1l2.7 6 6.3.6-4.8 4.3 1.4 6.3L10 15l-5.6 3.2 1.4-6.3L1 7.6l6.3-.6z"/></svg>Funktion des Kauorgans und inter­disziplinäre Zahnmedizin</h2>
    <p>„Funktion ist nicht alles. Aber ohne Funktion ist alles nichts!“ Sagte einst Prof. A. Marten (Zahnarzt, Gnathologie) und betonte die Bedeutung der Funktion des Kausystems. Sprechen, Kauen aber auch Körperhaltung und Stressmanagement gehören zu den Funktionen der Zähne. Ein gut funktionierendes Kauorgan (nach Prof. R. Lindqvist, interdisziplinäre Zahnmedizin) kann Stress bewältigen und mehr Leistung und Wohlbefinden bringen. Sehr oft erkennt man Funktionsstörungen daran, dass die Zähne nicht richtig zueinander passen oder Muskelverspannungen und Schmerzen im Kiefergelenk auftreten.</p>
  </div>

  <div class="divider"></div>

  <div class="section col-right">
    <h2><svg class="star" viewBox="0 0 20 20"><path fill="var(--green)" d="M10 1l2.7 6 6.3.6-4.8 4.3 1.4 6.3L10 15l-5.6 3.2 1.4-6.3L1 7.6l6.3-.6z"/></svg>Parodontitis und systemische Er­krankungen</h2>
    <p>Parodontitis (Entzündung des Zahnhalteapparats) ist eine der häufigsten chronischen Krankheiten weltweit und daher gut erforscht. Herzkrankheiten, Diabetes und Frühgeburtlichkeit sind einige der systemischen Krankheiten mit der Parodontitis in Zusammenhang steht. Zahnfleischbluten, Zahnlockerung, Zahnfleischschwund und Zahnverlust sind typische Begleiterscheinungen von Parodontitis. Eine systematische Parodontitis-Behandlung kann auch positive Auswirkungen auf die gesamte Gesundheit haben.</p>
  </div>

  <div class="section wide sec-3">
    <h2><svg class="star" viewBox="0 0 20 20"><path fill="var(--green)" d="M10 1l2.7 6 6.3.6-4.8 4.3 1.4 6.3L10 15l-5.6 3.2 1.4-6.3L1 7.6l6.3-.6z"/></svg>Zahnverlust und neurologische Auswirkung</h2>
    <p>Ein physiologisches Kausystem hat sehr feine Steuerungs- und Wahrnehmungsmöglichkeiten. Bei Zahnverlust werden diese Fähigkeiten weniger benötigt. Weniger gebrauchte Ressourcen werden von der Natur dementsprechend abgebaut. Studien zeigen, dass Menschen mit weniger Zähnen mehr Risiko zur Bildung von Demenz bergen.</p>
  </div>

  <div class="section wide sec-4">
    <h2><svg class="star" viewBox="0 0 20 20"><path fill="var(--green)" d="M10 1l2.7 6 6.3.6-4.8 4.3 1.4 6.3L10 15l-5.6 3.2 1.4-6.3L1 7.6l6.3-.6z"/></svg>Ganzheitliche Erklärungen</h2>
    <p>Die komplementäre Zahnheilkunde, sehr oft auch als ganzheitliche oder biologische Zahnheilkunde bezeichnet, versucht mit Hilfe von Meridianen (Traditionelle Chinesische Medizin), den Zusammenhang zwischen Zähnen und anderen Organen und Körperteilen zu erklären. Es gibt immer mehr Patienten und Zahnärzte die von dieser Theorie und deren Ergebnissen überzeugt sind. Aufgrund der wissenschaftlichen Lage ist eine ausführliche Aufklärung vor der Behandlung sehr ratsam.</p>
  </div>

  <div class="footer-band"></div>
  <div class="portrait" role="img" aria-label="Porträtfoto des neuen Zahnarztes"></div>
  <p class="footer-call">Für weitere Informationen rufen Sie uns in unserer Klinik an</p>
  <div class="footer-contact">
    <span><svg viewBox="0 0 16 22"><rect x="3" y="1" width="10" height="20" rx="2" fill="none" stroke="#111" stroke-width="2"/><circle cx="8" cy="17" r="1.2" fill="#111"/></svg>987-654-3210</span>
    <span><svg viewBox="0 0 16 22"><path fill="#111" d="M8 1a7 7 0 0 0-7 7c0 5 7 13 7 13s7-8 7-13a7 7 0 0 0-7-7zm0 10a3 3 0 1 1 0-6 3 3 0 0 1 0 6z"/></svg>youraddress, block no, building no.</span>
  </div>
</div>
</body>
</html>
```